Business Card Design for Marketing Firm

Looking for business card design for higher end marketing firm. Clean but impressionable/trendy. We are a marketing firm that represents manufacturers in the foodservice equipment and supply industry. Our customers are end users such has hotels, restaurants, country clubs, convention centers and casinos as well as distributors of restaurants supplies and equipment, and manufacturers of foodservice equipment and supplies.
Target Market(s)
Hotels, Restaurants, Supply & Equipment Distributors, Foodservice Manufacturers
Industry/Entity Type
Foodservice/Hospitality
Contact Information for Business Card
Name, Title, Contact Number, Email, Website, Social Media, Address
Requirements
Must have
- Clean & Simple but Serious and Impressionable

```html
<!DOCTYPE html>
<html lang="en">
<head>
<meta charset="utf-8">
<title>Meridian Hospitality Reps – Business Card</title>
<link rel="stylesheet" href="https://fonts.googleapis.com/css2?family=Open+Sans:wght@400;600;700&display=swap">
<style>
  :root {
    --backdrop: #dfe4ea;
    --card: #f1f3f6;
    --card-edge: #d3d9e1;
    --navy: #23265f;
    --ink: #34363c;
    --icon: #2c2f55;
  }
  * { margin: 0; padding: 0; box-sizing: border-box; }
  html, body { width: 1200px; height: 900px; overflow: hidden; }
  body {
    background: var(--backdrop);
    font-family: "Open Sans", Arial, sans-serif;
    position: relative;
  }
  .card {
    position: absolute;
    left: 80px; top: 154px;
    width: 1040px; height: 592px;
    background: var(--card);
    border: 1px solid var(--card-edge);
    border-radius: 22px;
    box-shadow: 0 10px 30px rgba(40, 50, 80, 0.12);
  }
  .brand {
    position: absolute;
    left: 40px; top: 150px;
    width: 460px;
    text-align: center;
    color: var(--navy);
    font-weight: 600;
  }
  .brand-mark {
    width: 58px; height: 58px;
    border-radius: 50%;
    background: var(--navy);
    margin: 0 auto 22px;
  }
  .brand-name {
    font-size: 38px;
    line-height: 1.15;
    letter-spacing: 1px;
  }
  .brand-sub {
    font-size: 26px;
    letter-spacing: 3px;
    margin-top: 4px;
  }
  .divider {
    position: absolute;
    left: 536px; top: 117px;
    width: 2px; height: 325px;
    background: var(--navy);
  }
  .contact {
    position: absolute;
    left: 569px; top: 110px;
    color: var(--ink);
  }
  .person-name {
    font-size: 38px;
    font-weight: 700;
    color: var(--navy);
    letter-spacing: 0.5px;
    line-height: 1.2;
  }
  .person-title {
    font-size: 26px;
    line-height: 1.3;
  }
  .address {
    font-size: 26px;
    line-height: 38px;
    margin-top: 32px;
  }
  .lines {
    list-style: none;
    margin-top: 26px;
    font-size: 26px;
    line-height: 38px;
  }
  .lines li { display: flex; align-items: center; gap: 8px; }
  .lines svg { width: 22px; height: 22px; flex: none; }
  .social {
    position: absolute;
    left: 0; right: 0; top: 516px;
    display: flex; justify-content: center; align-items: center; gap: 10px;
    font-size: 25px;
    color: var(--ink);
  }
  .social-dot {
    width: 16px; height: 16px; border-radius: 50%;
    background: var(--icon);
  }
</style>
</head>
<body>
  <div class="card">
    <div class="brand">
      <div class="brand-mark"></div>
      <div class="brand-name">MERIDIAN HOSPITALITY</div>
      <div class="brand-sub">REPS</div>
    </div>

    <div class="divider"></div>

    <div class="contact">
      <div class="person-name">DAREN WALCOTT</div>
      <div class="person-title">President</div>
      <div class="address">18230 Harbor View Dr<br>Seacliff CA 92710</div>
      <ul class="lines">
        <li>
          <svg viewBox="0 0 24 24" aria-hidden="true"><path fill="var(--icon)" d="M6.6 10.8a15.1 15.1 0 0 0 6.6 6.6l2.2-2.2a1 1 0 0 1 1-.25 11.4 11.4 0 0 0 3.6.57 1 1 0 0 1 1 1V20a1 1 0 0 1-1 1A17 17 0 0 1 3 4a1 1 0 0 1 1-1h3.5a1 1 0 0 1 1 1c0 1.25.2 2.45.57 3.57a1 1 0 0 1-.25 1z"/></svg>
          555-310-4827
        </li>
        <li>
          <svg viewBox="0 0 24 24" aria-hidden="true"><rect x="3" y="6" width="18" height="12" rx="1.5" fill="var(--icon)"/><path d="M3.5 7l8.5 6 8.5-6" fill="none" stroke="var(--card)" stroke-width="1.6"/></svg>
          info@meridianhospreps.com
        </li>
        <li>
          <svg viewBox="0 0 24 24" aria-hidden="true"><circle cx="12" cy="12" r="9" fill="none" stroke="var(--icon)" stroke-width="2"/><ellipse cx="12" cy="12" rx="4" ry="9" fill="none" stroke="var(--icon)" stroke-width="1.6"/><path d="M3 12h18" stroke="var(--icon)" stroke-width="1.6"/></svg>
          www.meridianhospreps.com
        </li>
      </ul>
    </div>

    <div class="social">
      <span class="social-dot"></span>
      <span>@meridianhospreps</span>
    </div>
  </div>
</body>
</html>
```